Website Design for VeteranLedger.com

VeteranLedger.com offers military researchers, reunion coordinators, military museums and others access to over 13 million military personnel records including the Internet's only 1988 Desert Service Roll Archive, Desert Service Troop Lists and Jungle Campaign Roll Archive.

We are currently going through a rebranding and website redesign. We require a modern, "web 2.0" design consistent with the quality expected of most technology start-ups. Please use the logo below for your design:

http://pbraith.hostlark.net/vlgr_content/veteranLedger_LOGO.jpg [JPG]
http://pbraith.hostlark.net/vlgr_content/veteranLedger_LOGO.psd [PSD]

```html
<!DOCTYPE html>
<html lang="en">
<head>
<meta charset="utf-8">
<title>VeteranLedger.com — Search Military Records</title>
<link href="https://fonts.googleapis.com/css2?family=Ropa+Sans&family=Roboto:wght@400;500&display=swap" rel="stylesheet">
<style>
:root{
  --blue:#3a8ad6;
  --blue-dark:#1f5fa8;
  --ink:#333;
  --muted:#666;
  --white:#fff;
  --strip:#f4f4f4;
  --footer:#dedede;
  --field-border:#c9c9c9;
}
*{box-sizing:border-box;margin:0;padding:0}
html,body{width:1200px;height:677px;overflow:hidden}
body{position:relative;font-family:"Roboto",sans-serif;color:var(--ink);background:var(--white)}
.hero{position:absolute;left:0;top:0;width:1200px;height:397px;
  background:linear-gradient(100deg,#3b3f3b 0%,#6f706a 30%,#b9b7ad 55%,#e4e1d6 75%,#cfcabb 100%)}
.hero-ground{position:absolute;left:0;bottom:0;width:1200px;height:150px;
  background:linear-gradient(180deg,rgba(40,42,35,0) 0%,rgba(30,32,26,.85) 60%,#1f211b 100%)}
.site-header{position:absolute;left:0;top:0;width:1200px;height:72px}
.brand{position:absolute;left:220px;top:22px;display:flex;align-items:center;gap:10px}
.brand-mark{width:26px;height:26px;background:#c9323a}
.brand-name{font-family:"Ropa Sans",sans-serif;font-size:26px;color:var(--white);letter-spacing:.5px}
.main-nav{position:absolute;top:30px;left:534px;display:flex;gap:0}
.main-nav a{font-family:"Ropa Sans",sans-serif;font-size:12px;color:#111;text-decoration:none;text-transform:uppercase}
.nav-home{position:absolute;left:0}
.nav-db{position:absolute;left:64px}
.nav-res{position:absolute;left:139px}
.nav-about{position:absolute;left:225px}
.nav-contact{position:absolute;left:288px;white-space:nowrap}
.login-btn{position:absolute;left:910px;top:23px;width:76px;height:26px;border-radius:3px;
  background:linear-gradient(#6d6d6d,#444);color:var(--white);font-size:11px;text-align:center;line-height:26px;
  font-family:"Ropa Sans",sans-serif;border:1px solid #333}
.search-card{position:absolute;left:252px;top:125px;width:265px;height:218px;background:var(--white);
  box-shadow:0 2px 8px rgba(0,0,0,.35)}
.search-head{height:65px;border-bottom:1px solid #e4e4e4;display:flex;align-items:center;padding-left:38px;gap:12px}
.search-head p{font-family:"Ropa Sans",sans-serif;font-size:14px;color:var(--muted);line-height:16px}
.field{position:absolute;left:37px;width:137px;height:30px;border:1px solid var(--field-border);
  font-size:9px;color:#999;padding:10px 8px;border-radius:2px}
.field-first{top:82px}.field-last{top:128px}
.find-btn{position:absolute;left:162px;top:173px;width:62px;height:26px;background:linear-gradient(#4a9be3,var(--blue-dark));
  color:var(--white);font-size:10px;text-align:center;line-height:26px;border-radius:3px;font-family:"Ropa Sans",sans-serif}
.hero-copy{position:absolute;left:572px;top:160px;width:400px}
.hero-copy h1{font-family:"Ropa Sans",sans-serif;font-weight:400;font-size:34px;line-height:38px;color:var(--blue)}
.hero-copy p{font-size:13px;color:var(--white);margin-top:10px}
.read-more{display:inline-block;margin-top:14px;width:84px;height:30px;background:linear-gradient(#4a9be3,var(--blue-dark));
  color:var(--white);font-size:9px;text-align:center;line-height:30px;border-radius:3px;text-transform:uppercase}
.features{position:absolute;left:0;top:397px;width:1200px;height:93px;background:var(--strip);border-bottom:1px solid #ddd}
.feature{position:absolute;top:18px}
.feature h2{font-family:"Ropa Sans",sans-serif;font-weight:400;font-size:18px;color:var(--blue);margin-left:32px}
.feature p{font-size:11px;color:var(--muted);line-height:15px;margin-top:6px}
.feature svg{position:absolute;left:0;top:0}
.f-db{left:220px}.f-books{left:408px}.f-join{left:600px}
.promo{position:absolute;left:768px;top:408px;display:flex;gap:12px}
.promo-photo{width:72px;height:72px;border:3px solid var(--blue);background:linear-gradient(#8fb3cf,#c8a98c)}
.promo h3{font-family:"Ropa Sans",sans-serif;font-weight:400;font-size:17px;line-height:19px;color:var(--blue-dark)}
.promo p{font-size:10px;color:var(--muted);line-height:13px;margin-top:3px}
.gallery{position:absolute;left:0;top:490px;width:1200px;height:150px;display:grid;
  grid-template-columns:repeat(13,1fr);grid-template-rows:repeat(2,1fr);gap:2px;background:#fff}
.gallery span{display:block}
.t1{background:linear-gradient(#8a8264,#5b5640)}.t2{background:linear-gradient(#a9a08a,#6e6650)}
.t3{background:linear-gradient(#c7b2a6,#8e7e74)}.t4{background:linear-gradient(#6b6b62,#3d3d38)}
.t5{background:linear-gradient(#7f8a94,#515a60)}.t6{background:linear-gradient(#9e9b88,#5c5a4c)}
.site-footer{position:absolute;left:0;top:640px;width:1200px;height:37px;background:var(--footer);
  font-size:10px;color:var(--muted);line-height:37px}
.footer-links{position:absolute;left:229px}
.copyright{position:absolute;left:632px}
</style>
</head>
<body>
<section class="hero">
  <div role="img" aria-label="Silhouette of a soldier walking through tall grass at sunrise" style="position:absolute;inset:0"></div>
  <div class="hero-ground"></div>

  <header class="site-header">
    <div class="brand"><span class="brand-mark"></span><span class="brand-name">VeteranLedger</span></div>
    <nav class="main-nav">
      <a class="nav-home" href="#">Home</a>
      <a class="nav-db" href="#">Database</a>
      <a class="nav-res" href="#">Resources</a>
      <a class="nav-about" href="#">About</a>
      <a class="nav-contact" href="#">Contact Us</a>
    </nav>
    <div class="login-btn">LOGIN ▾</div>
  </header>

  <form class="search-card">
    <div class="search-head">
      <svg width="30" height="30" viewBox="0 0 30 30"><circle cx="12" cy="12" r="8.5" fill="none" stroke="#2a7ccc" stroke-width="4"/><line x1="18" y1="18" x2="27" y2="27" stroke="#2a7ccc" stroke-width="5" stroke-linecap="round"/></svg>
      <p>Search Now To Find<br>Your Ancestors</p>
    </div>
    <div class="field field-first">First Name</div>
    <div class="field field-last">Last name</div>
    <div class="find-btn">FIND</div>
  </form>

  <div class="hero-copy">
    <h1>Family Connections Last Forever</h1>
    <p>Gather and preserve your family story here</p>
    <a class="read-more" href="#">Read More</a>
  </div>
</section>

<section class="features">
  <div class="feature f-db">
    <svg width="22" height="22" viewBox="0 0 22 22"><rect x="1" y="1" width="14" height="14" fill="none" stroke="#333" stroke-width="2"/><rect x="6" y="6" width="14" height="14" fill="#fff" stroke="#333" stroke-width="2"/></svg>
    <h2>Database</h2>
    <p>1988 Desert Service Troop Lists<br>Jungle Campaign Veterans</p>
  </div>
  <div class="feature f-books">
    <svg width="22" height="22" viewBox="0 0 22 22"><rect x="1" y="1" width="13" height="16" fill="none" stroke="#333" stroke-width="2"/><rect x="7" y="5" width="13" height="16" fill="#fff" stroke="#333" stroke-width="2"/></svg>
    <h2>Books</h2>
    <p>How to Locate Military...<br>World War II Military Records...</p>
  </div>
  <div class="feature f-join">
    <svg width="22" height="22" viewBox="0 0 22 22"><circle cx="11" cy="6" r="5" fill="#222"/><path d="M1 21c0-6 4-9 10-9s10 3 10 9z" fill="#222"/></svg>
    <h2>Join Our Site</h2>
    <p>Join our Site for free and<br>Get acess to our database</p>
  </div>
</section>

<div class="promo">
  <div class="promo-photo" role="img" aria-label="Family portrait with a veteran"></div>
  <div>
    <h3>Family connections<br>last forever.</h3>
    <p>Gather and preserve your<br>family story here.</p>
  </div>
</div>

<div class="gallery" role="img" aria-label="Mosaic of military photographs: troops, aircraft, memorials, tanks and officers">
  <span class="t1"></span><span class="t2"></span><span class="t3"></span><span class="t4"></span><span class="t6"></span><span class="t1"></span><span class="t4"></span><span class="t3"></span><span class="t2"></span><span class="t4"></span><span class="t6"></span><span class="t1"></span><span class="t2"></span>
  <span class="t5"></span><span class="t2"></span><span class="t6"></span><span class="t4"></span><span class="t5"></span><span class="t2"></span><span class="t4"></span><span class="t5"></span><span class="t1"></span><span class="t3"></span><span class="t5"></span><span class="t2"></span><span class="t4"></span>
</div>

<footer class="site-footer">
  <span class="footer-links">Home | Databases | Join | Books | Advertise | About | FAQ | Contact</span>
  <span class="copyright">Copyright © 2010 Service Records Group, Inc. All Rights Reserved.</span>
</footer>
</body>
</html>
```